New emergency medical service needs a marketing flyer for prospective customers

We need a tri fold brochure on an 8.5 X 11 stock for a new emergency medical service in Pennsylvania. We provide basic first aid and now Covid-19 pre screening and temperature monitoring for special events, large gatherings and businesses. Examples of these would be but not limited to: Sporting events, carnivals, festivals, craft shows, warehouses, churches, manufacturing facilities, industrial buildings, large construction sites, multi occupancy officer buildings. The market for this is pretty much untouched and endless. we would like to use gray as the back ground color and obviously our logo. The final design should grab their attention and communicate the importance of having trained and certified professionals at their event or facility. We want to give them that piece of mind they are in good hands with us.

Target Market(s)

primary focus is going to be on businesses with large offices, large buildings or lots of foot traffic in and out of the building

Requirements
Must have
• gray background, pictures, company phone # , company web site, and contact email address. I will provide all that information to the winner to add at the end.
Nice to have
• pictures that covers the whole front cover with logo at top

```html
<!DOCTYPE html>
<html lang="en">
<head>
<meta charset="utf-8">
<title>Halvecta Tri-Fold Brochure</title>
<link href="https://fonts.googleapis.com/css2?family=Roboto:wght@300;400;500;700&family=Montserrat:ital,wght@0,400;1,400&display=swap" rel="stylesheet">
<style>
  :root {
    --teal: #13b3a0;
    --navy: #2b2f8e;
    --ink: #1c1c1c;
    --text-grey: #9a9a9a;
    --stage-light: #d9dadc;
    --stage-dark: #58585a;
    --white: #ffffff;
  }
  * { margin: 0; padding: 0; box-sizing: border-box; }
  html, body { width: 818px; height: 1200px; overflow: hidden; }
  body {
    position: relative;
    background: linear-gradient(to bottom, var(--stage-light) 0, var(--stage-light) 912px, var(--stage-dark) 912px);
    font-family: "Roboto", sans-serif;
  }
  .sheet {
    position: absolute; left: 86px; width: 647px; height: 502px;
    background: var(--white); overflow: hidden;
    box-shadow: 4px 5px 8px rgba(0,0,0,.35);
  }
  .sheet--outside { top: 86px; }
  .sheet--inside { top: 612px; }
  .panel { position: absolute; top: 0; height: 502px; overflow: hidden; }
  .panel--one { left: 0; width: 214px; }
  .panel--two { left: 214px; width: 214px; }
  .panel--three { left: 428px; width: 219px; }
  .panel svg.art { position: absolute; left: 0; top: 0; }

  .eyebrow { font-size: 11px; color: var(--ink); letter-spacing: .2px; }
  .headline { font-weight: 700; font-size: 26px; color: var(--teal); line-height: 1; letter-spacing: -.2px; }
  .body-copy { font-family: "Montserrat", sans-serif; font-size: 5.6px; line-height: 1.9; color: var(--text-grey); }

  /* outside panel one */
  .intro { position: absolute; left: 23px; top: 40px; width: 185px; }
  .intro .headline { margin-top: 3px; margin-bottom: 14px; }
  .intro .body-copy { margin-bottom: 8px; }

  /* wordmarks */
  .wordmark { position: absolute; display: flex; align-items: center; gap: 7px; font-weight: 700; font-size: 32px; letter-spacing: .3px; }
  .wordmark__dot { width: 13px; height: 13px; border-radius: 50%; }
  .wordmark--light { left: 18px; top: 100px; color: var(--white); }
  .wordmark--light .wordmark__dot { background: var(--white); }
  .wordmark--brand { left: 16px; top: 420px; color: var(--navy); }
  .wordmark--brand .wordmark__dot { background: var(--navy); }

  /* outside panel two */
  .contact { position: absolute; left: 27px; top: 318px; color: var(--white); }
  .contact__label { font-weight: 700; font-size: 12px; margin-top: 9px; }
  .contact__label:first-child { margin-top: 0; }
  .contact__value { font-size: 9.3px; line-height: 1.35; font-weight: 300; }

  /* inside panel one */
  .about { position: absolute; left: 15px; top: 224px; width: 192px; }
  .about__title { font-weight: 700; font-size: 27px; color: var(--teal); }
  .about__lead { font-family: "Montserrat", sans-serif; font-style: italic; font-size: 6.6px; line-height: 1.65; color: #666; margin: 5px 0 9px; }
  .about .body-copy { font-style: italic; margin-bottom: 8px; color: #b0b0b0; }

  /* inside panel two */
  .process { position: absolute; left: 0; top: 0; width: 214px; height: 502px; background: var(--teal); }
  .process__head { position: absolute; left: 22px; top: 31px; }
  .process__head .eyebrow { color: var(--white); }
  .process__head .headline { color: var(--white); font-size: 22px; margin-top: 2px; }
  .step { position: absolute; left: 21px; width: 185px; display: flex; gap: 10px; align-items: flex-start; }
  .step__num { flex: none; width: 30px; height: 30px; border-radius: 50%; background: var(--ink); color: var(--teal); font-size: 20px; display: flex; align-items: center; justify-content: center; }
  .step__text { font-family: "Montserrat", sans-serif; font-size: 5.2px; line-height: 1.75; color: var(--white); padding-top: 1px; }
  .step--1 { top: 74px; } .step--2 { top: 117px; } .step--3 { top: 398px; } .step--4 { top: 441px; }
  .team-photo { position: absolute; left: 12px; top: 171px; width: 190px; height: 190px; border-radius: 50%; border: 7px solid var(--ink); background: radial-gradient(circle at 45% 40%, #e8d8cf, #8f8a86 55%, #3e3b3a); }

  /* inside panel three */
  .services__bg { position: absolute; inset: 0; background: linear-gradient(160deg, #2f3596 0%, #2a2d8a 45%, #262a7c 100%); }
  .services__photo { position: absolute; left: 40px; top: 60px; width: 179px; height: 442px; background: radial-gradient(ellipse at 60% 30%, rgba(70,60,130,.7), rgba(43,47,142,0) 70%); }
  .services__corner { position: absolute; left: 170px; top: -30px; width: 80px; height: 80px; border-radius: 14px; background: var(--teal); transform: rotate(45deg); }
  .services__head { position: absolute; left: 20px; top: 63px; color: var(--white); }
  .services__kicker { font-size: 12px; }
  .services__title { font-weight: 700; font-size: 26px; line-height: 1; }
  .service { position: absolute; left: 20px; width: 192px; display: flex; gap: 12px; }
  .service__icon { flex: none; width: 30px; height: 30px; display: flex; align-items: center; justify-content: center; position: relative; }
  .service__icon::before { content: ""; position: absolute; inset: 3px; background: var(--teal); border-radius: 7px; transform: rotate(45deg); }
  .service__icon svg { position: relative; }
  .service__name { font-weight: 700; font-size: 7.5px; color: var(--white); margin-top: 1px; }
  .service__text { font-family: "Montserrat", sans-serif; font-size: 5.2px; line-height: 1.6; color: #c6c8e8; }
</style>
</head>
<body>

<section class="sheet sheet--outside">

  <div class="panel panel--one">
    <div class="intro">
      <p class="eyebrow">TEXT HERE</p>
      <h2 class="headline">LOREM IPSUM</h2>
      <p class="body-copy">Our certified medics screen every guest at the door and keep your event running safely all day.</p>
      <p class="body-copy">Fast first aid on site.</p>
      <p class="body-copy">We monitor temperatures, log results and report to your team in real time without delay.</p>
      <p class="body-copy">Trained staff for any crowd.</p>
      <p class="body-copy">Calm care you can count on.</p>
    </div>
    <svg class="art" width="214" height="502" viewBox="0 0 214 502">
      <polygon points="0,380 214,258 214,502 0,502" fill="#b9c4cc" role="img" aria-label="Photo of masked office staff working at a meeting table"/>
      <polygon points="0,366 214,247 214,251 0,370" fill="var(--teal)"/>
      <polygon points="0,372 214,252 214,258 0,380" fill="var(--navy)"/>
    </svg>
  </div>

  <div class="panel panel--two" style="background:linear-gradient(170deg,#1a8f7f 0%,#14a592 40%,#0f7d70 100%);">
    <div role="img" aria-label="Photo of a hand holding an infrared thermometer" style="position:absolute;inset:0;background:radial-gradient(ellipse at 45% 45%,rgba(10,60,55,.45),rgba(0,0,0,0) 60%);"></div>
    <div class="wordmark wordmark--light"><span class="wordmark__dot"></span>Halvecta</div>
    <div class="contact">
      <p class="contact__label">PHONE</p>
      <p class="contact__value">(555)-010-2387<br>(555)-010-4419</p>
      <p class="contact__label">EMAIL</p>
      <p class="contact__value">hello@halvecta.example</p>
      <p class="contact__label">ADDRESS</p>
      <p class="contact__value">418 Larkspur Avenue, Suite 2</p>
      <p class="contact__label">WEBSITE</p>
      <p class="contact__value">halvecta.example</p>
    </div>
  </div>

  <div class="panel panel--three">
    <svg class="art" width="219" height="502" viewBox="0 0 219 502">
      <polygon points="0,0 219,0 219,40 0,240" fill="var(--navy)"/>
      <polygon points="219,40 219,215 120,120" fill="var(--teal)"/>
      <polygon points="219,330 219,400 170,365" fill="var(--teal)"/>
      <g role="img" aria-label="Photos of temperature screening and masked business people">
        <rect x="84" y="80" width="84" height="84" rx="9" transform="rotate(45 126 122)" fill="#d7cfcf" stroke="#fff" stroke-width="3"/>
        <rect x="12" y="182" width="78" height="78" rx="9" transform="rotate(45 51 221)" fill="#9ea6b3" stroke="#fff" stroke-width="3"/>
        <rect x="142" y="182" width="78" height="78" rx="9" transform="rotate(45 181 221)" fill="#c9b4ad" stroke="#fff" stroke-width="3"/>
        <rect x="70" y="255" width="114" height="114" rx="11" transform="rotate(45 127 312)" fill="#8f97a6" stroke="#fff" stroke-width="3"/>
      </g>
    </svg>
    <div class="wordmark wordmark--brand"><span class="wordmark__dot"></span>Halvecta</div>
  </div>

</section>

<section class="sheet sheet--inside">

  <div class="panel panel--one">
    <svg class="art" width="214" height="502" viewBox="0 0 214 502">
      <polygon points="144,0 208,0 170,27" fill="var(--navy)"/>
      <rect x="-70" y="-80" width="220" height="220" rx="26" transform="rotate(45 40 30)" fill="#7fd3e0" stroke="#fff" stroke-width="4" role="img" aria-label="Photo of face mask, gloves, sanitizer and stethoscope"/>
      <rect x="128" y="114" width="72" height="72" rx="11" transform="rotate(45 164 150)" fill="var(--teal)"/>
      <rect x="17" y="160" width="24" height="24" rx="4" transform="rotate(45 29 172)" fill="var(--teal)" stroke="#fff" stroke-width="3"/>
      <rect x="148" y="420" width="120" height="120" rx="20" transform="rotate(45 208 480)" fill="#f3f3f5"/>
      <rect x="51" y="403" width="58" height="58" rx="12" transform="rotate(45 80 432)" fill="var(--teal)"/>
      <rect x="2" y="413" width="80" height="80" rx="14" transform="rotate(45 42 453)" fill="var(--navy)"/>
    </svg>
    <div class="about">
      <h2 class="about__title">About Us</h2>
      <p class="about__lead">An Employee-Owned Company With A Client-First Culture And A Commitment To Remain Independent.</p>
      <p class="body-copy">We bring trained first responders to offices, plants and venues so people stay safe and work can go on.</p>
      <p class="body-copy">Every medic is certified and ready for your site.</p>
    </div>
  </div>

  <div class="panel panel--two">
    <div class="process">
      <div class="process__head">
        <p class="eyebrow">TEXT HERE</p>
        <h2 class="headline">LOREM IPSUM</h2>
      </div>
      <div class="step step--1"><span class="step__num">1</span><p class="step__text">Certified medics screen each visitor and keep clear records for your team every day.</p></div>
      <div class="step step--2"><span class="step__num">2</span><p class="step__text">Touchless temperature checks at every entry point keep lines moving and people at ease.</p></div>
      <div class="team-photo" role="img" aria-label="Photo of a masked team gathered around a laptop"></div>
      <div class="step step--3"><span class="step__num">3</span><p class="step__text">First aid stations are set up fast and staffed through the whole event schedule.</p></div>
      <div class="step step--4"><span class="step__num">4</span><p class="step__text">Clear reports after each shift help you plan safer days for staff and guests.</p></div>
    </div>
  </div>

  <div class="panel panel--three">
    <div class="services__bg"></div>
    <div class="services__photo" role="img" aria-label="Photo of a man on the phone, tinted blue"></div>
    <div class="services__corner"></div>
    <div class="services__head">
      <p class="services__kicker">Our Best</p>
      <h2 class="services__title">Services</h2>
    </div>

    <div class="service" style="top:126px">
      <span class="service__icon"><svg width="12" height="12" viewBox="0 0 12 12"><circle cx="5" cy="5" r="3.3" fill="none" stroke="#fff" stroke-width="1.4"/><line x1="7.4" y1="7.4" x2="11" y2="11" stroke="#fff" stroke-width="1.6"/></svg></span>
      <div><p class="service__name">Service Name</p><p class="service__text">Short note on this service and how our team supports your site.</p></div>
    </div>
    <div class="service" style="top:178px">
      <span class="service__icon"><svg width="12" height="12" viewBox="0 0 12 12"><polygon points="1,4 5,4 10,1 10,11 5,8 1,8" fill="#fff"/></svg></span>
      <div><p class="service__name">Service Name</p><p class="service__text">Short note on this service and how our team supports your site.</p></div>
    </div>
    <div class="service" style="top:230px">
      <span class="service__icon"><svg width="12" height="12" viewBox="0 0 12 12"><rect x="1" y="3.5" width="10" height="7" rx="1" fill="#fff"/><rect x="4" y="1.5" width="4" height="2.5" fill="none" stroke="#fff" stroke-width="1"/></svg></span>
      <div><p class="service__name">Service Name</p><p class="service__text">Short note on this service and how our team supports your site.</p></div>
    </div>
    <div class="service" style="top:282px">
      <span class="service__icon"><svg width="12" height="12" viewBox="0 0 12 12"><circle cx="6" cy="6" r="3.5" fill="none" stroke="#fff" stroke-width="2.2" stroke-dasharray="2 1.2"/><circle cx="6" cy="6" r="1.2" fill="#fff"/></svg></span>
      <div><p class="service__name">Service Name</p><p class="service__text">Short note on this service and how our team supports your site.</p></div>
    </div>
    <div class="service" style="top:334px">
      <span class="service__icon"><svg width="12" height="12" viewBox="0 0 12 12"><circle cx="6" cy="6" r="4.5" fill="none" stroke="#fff" stroke-width="1.3"/><polyline points="6,3.5 6,6 8,7" fill="none" stroke="#fff" stroke-width="1.2"/></svg></span>
      <div><p class="service__name">Service Name</p><p class="service__text">Short note on this service and how our team supports your site.</p></div>
    </div>
    <div class="service" style="top:386px">
      <span class="service__icon"><svg width="12" height="12" viewBox="0 0 12 12"><polygon points="6,1 11,3.5 6,6 1,3.5" fill="#fff"/><polyline points="1,6 6,8.5 11,6" fill="none" stroke="#fff" stroke-width="1.1"/><polyline points="1,8.5 6,11 11,8.5" fill="none" stroke="#fff" stroke-width="1.1"/></svg></span>
      <div><p class="service__name">Service Name</p><p class="service__text">Short note on this service and how our team supports your site.</p></div>
    </div>
    <div class="service" style="top:438px">
      <span class="service__icon"><svg width="12" height="12" viewBox="0 0 12 12"><path d="M3 1.5 L5 4 L4 5 Q5 7.5 7 8 L8 7 L10.5 9 L9 11 Q3 10 1 3 Z" fill="#fff"/></svg></span>
      <div><p class="service__name">Service Name</p><p class="service__text">Short note on this service and how our team supports your site.</p></div>
    </div>
  </div>

</section>

</body>
</html>
```